Informative Infografiken für Matratzenhersteller
Zielgruppe
Produzent von Matratzen, Zielgruppe ist daher jeder der eine neue Matratze benötigt
Aufgabenstellung
Die Infografik soll auf einer Webseite implementiert werden. Es wäre daher schön, wenn die CI Farben #63b32f und #343A40 eingebunden werden könnten.
Die Infografik soll schnell Informationen zu folgende Themen ersichtlich machen: Härtegrad, Raumgewicht, Matratze für verschiedene Schlaftypen

```html
<!DOCTYPE html>
<html lang="de">
<head>
<meta charset="utf-8">
<title>Matratzen-Ratgeber: Härtegrad, Raumgewicht, Schlaftyp</title>
<link href="https://fonts.googleapis.com/css2?family=Roboto+Condensed:wght@300;400&family=Roboto:wght@300;400&display=swap" rel="stylesheet">
<style>
  :root {
    --page-bg: #e8e5e4;
    --panel-bg: #c4c4bf;
    --ink: #343a40;
    --ink-soft: #4f4f4f;
    --text: #2a2a2a;
    --title: #1e1e1e;
    --green: #63b32f;
    --green-1: #55ae35;
    --green-2: #7bb45a;
    --green-3: #8fbb72;
    --green-4: #9bbf85;
    --white: #ffffff;
  }
  * { margin: 0; padding: 0; box-sizing: border-box; }
  html, body { width: 1200px; height: 926px; overflow: hidden; }
  body { background: var(--page-bg); font-family: "Roboto", sans-serif; color: var(--ink); position: relative; }

  .panel { position: absolute; top: 41px; width: 345px; height: 841px; background: var(--panel-bg); overflow: hidden; }
  .panel--hardness { left: 36px; }
  .panel--density { left: 423px; }
  .panel--sleeper { left: 806px; }

  .panel__art {
    position: absolute; border-radius: 38px 38px 22px 22px;
    background: linear-gradient(180deg, #3c4247 0%, var(--ink) 70%);
  }
  .panel__chart { position: absolute; left: 0; top: 0; }

  .panel__title {
    position: absolute; top: 522px;
    font-family: "Roboto Condensed", sans-serif; font-weight: 400; font-size: 31px;
    color: var(--title); line-height: 34px; white-space: nowrap;
  }
  .panel__text {
    position: absolute; font-size: 16.5px; line-height: 21.8px; font-weight: 300;
    color: var(--text); white-space: nowrap;
  }

  .panel--hardness .panel__title, .hardness__intro, .hardness__scale { left: 40px; }
  .hardness__intro { top: 566px; }
  .hardness__scale { top: 719px; }

  .panel--density .panel__title { left: 36px; }
  .density__intro {
    left: 36px; top: 567px;
    font-family: "Roboto Condensed", sans-serif; font-weight: 300;
    font-size: 17px; line-height: 20.2px; letter-spacing: -0.3px; color: var(--ink-soft);
  }
  .density__table { left: 36px; top: 729px; }
  .density__row { display: grid; grid-template-columns: 23px 22px 99px 49px 37px auto; height: 21.8px; }

  .panel--sleeper .panel__title { left: 34px; }
  .sleeper__list { left: 34px; top: 566px; list-style: none; }
  .sleeper__list li { margin-bottom: 10.2px; }
  .sleeper__list span { display: block; padding-left: 14px; }
</style>
</head>
<body>

<section class="panel panel--hardness">
  <div class="panel__art" role="img" aria-label="Illustration: Matratze mit Kettlebell-Gewicht" style="left:35px; top:33px; width:276px; height:195px;"></div>

  <svg class="panel__chart" width="345" height="560" viewBox="0 0 345 560" role="img" aria-label="Härtegrade H2 bis H5">
    <g font-family="Roboto Condensed, sans-serif" font-size="27" fill="var(--white)" text-anchor="middle">
      <polygon points="43,364 75,339 107,364 107,509 43,509" fill="var(--green-4)"/>
      <polygon points="108,344 140,317 172,344 172,509 108,509" fill="var(--green-3)"/>
      <polygon points="173,326 205,302 237,326 237,509 173,509" fill="var(--green-2)"/>
      <polygon points="238,304 270,279 302,304 302,509 238,509" fill="var(--green-1)"/>
      <text x="73" y="393">H2</text>
      <text x="141" y="369">H3</text>
      <text x="207" y="353">H4</text>
      <text x="272" y="334">H5</text>
    </g>
  </svg>

  <h2 class="panel__title">Härtegrad</h2>
  <p class="panel__text hardness__intro">Härtegrad nach Body Mass Index<br>(BMI) bestimmen. Weil neben dem<br>Körpergewicht auch die Körperlänge<br>eine Rolle spielt, können Sie den rich-<br>tigen Härtegrad auch nach BMI aus-<br>wählen.</p>
  <p class="panel__text hardness__scale">H3 = Gewicht bis 100kg = BMI bis 30<br>H4 = Gewicht bis 130kg = BMI bis 35<br>H5 = Gewicht bis 140kg = BMI bis 40</p>
</section>

<section class="panel panel--density">
  <div class="panel__art" role="img" aria-label="Illustration: zwei Matratzen auf einer Wippe" style="left:23px; top:77px; width:291px; height:136px;"></div>

  <svg class="panel__chart" width="345" height="560" viewBox="0 0 345 560" role="img" aria-label="Raumgewicht und Qualitätsstufen">
    <g font-family="Roboto Condensed, sans-serif" fill="var(--white)">
      <polygon points="25,280 63,260 102,280 63,300 25,300" fill="#a9c795"/>
      <polygon points="25,280 63,300 63,336 25,320" fill="#a0c48b"/>
      <polygon points="63,300 96,288 96,324 63,336" fill="#8eb275"/>
      <polygon points="96,280 144,280 155,300 144,320 96,320" fill="var(--green-4)"/>
      <text x="103" y="311" font-size="26">20 - 25</text>
      <polygon points="25,329 63,350 63,386 25,370" fill="#a0c48b"/>
      <polygon points="63,350 96,338 96,374 63,386" fill="#80a86a"/>
      <polygon points="96,330 144,330 155,350 144,370 96,370" fill="var(--green-3)"/>
      <text x="103" y="361" font-size="26">40</text>
      <polygon points="25,378 63,398 63,434 25,418" fill="#9cc286"/>
      <polygon points="63,398 96,386 96,422 63,434" fill="#6d9a52"/>
      <polygon points="96,379 144,379 155,399 144,419 96,419" fill="var(--green-2)"/>
      <text x="104" y="410" font-size="26">50 - 60</text>
      <polygon points="25,427 63,447 63,485 25,468" fill="#8cc265"/>
      <polygon points="63,447 96,435 96,472 63,485" fill="#3d8a2e"/>
      <polygon points="96,429 144,429 155,449 144,469 96,469" fill="var(--green-1)"/>
      <text x="104" y="460" font-size="26">75</text>

      <g font-size="24" text-anchor="middle">
        <circle cx="221" cy="301" r="21" fill="var(--green-4)"/><text x="221" y="310">4</text>
        <circle cx="221" cy="351" r="21" fill="var(--green-3)"/><text x="221" y="360">3</text>
        <circle cx="221" cy="400" r="21" fill="var(--green-2)"/><text x="221" y="409">2</text>
        <circle cx="221" cy="450" r="21" fill="var(--green-1)"/><text x="221" y="459">1</text>
      </g>
      <g font-family="Roboto, sans-serif" font-weight="300" font-size="16.5" fill="var(--text)">
        <text x="254" y="297">Niedriger</text><text x="254" y="316">Standard</text>
        <text x="254" y="347">Gute</text><text x="254" y="366">Qualität</text>
        <text x="254" y="397">Sehr hohe</text><text x="254" y="416">Qualität</text>
        <text x="254" y="448">Exzellente</text><text x="254" y="467">Qualität</text>
      </g>
    </g>
  </svg>

  <h2 class="panel__title">Raumgewicht</h2>
  <p class="panel__text density__intro">Das Raumgewicht gilt als Kennzahl für<br>die Haltbarkeit einer Matratze und gibt an,<br>wie viel Kilogramm Rohmasse in einem<br>Kubikmeter Schaumstoff aufgeschäumt<br>wurden. Je höher, desto schwerer der<br>Schaumstoff und umso höher Langlebig-<br>keit der Matratze.</p>
  <div class="panel__text density__table">
    <div class="density__row"><span>4</span><span>=</span><span>Haltbarkeit:</span><span>etwa</span><span>1-2</span><span>Jahre</span></div>
    <div class="density__row"><span>3</span><span>=</span><span>Haltbarkeit:</span><span>etwa</span><span>6-8</span><span>Jahre</span></div>
    <div class="density__row"><span>2</span><span>=</span><span>Haltbarkeit:</span><span>etwa</span><span>10</span><span>Jahre</span></div>
    <div class="density__row"><span>1</span><span>=</span><span>Haltbarkeit:</span><span>über</span><span>10</span><span>Jahre</span></div>
  </div>
</section>

<section class="panel panel--sleeper">
  <div class="panel__art" role="img" aria-label="Illustration: schlafende Figur auf einer Matratze" style="left:33px; top:84px; width:274px; height:131px; background:linear-gradient(180deg, #4f7a3a 0%, var(--ink) 65%);"></div>

  <svg class="panel__chart" width="345" height="560" viewBox="0 0 345 560" role="img" aria-label="Schlaftypen: Bauch, Fötus, Rücken, Seite">
    <path d="M34,287 A99,99 0 0 1 34,484" fill="none" stroke="var(--green-1)" stroke-width="4"/>
    <g font-family="Roboto Condensed, sans-serif" font-size="22" fill="var(--white)" text-anchor="middle">
      <rect x="119" y="284" width="150" height="38" rx="19" fill="var(--green-1)"/><text x="194" y="311">Bauch</text>
      <rect x="151" y="337" width="150" height="38" rx="19" fill="var(--green-2)"/><text x="220" y="364">Fötus</text>
      <rect x="150" y="391" width="151" height="38" rx="19" fill="var(--green-3)"/><text x="228" y="418">Rücken</text>
      <rect x="129" y="445" width="150" height="38" rx="19" fill="var(--green-4)"/><text x="189" y="472">Seite</text>
    </g>
  </svg>

  <h2 class="panel__title">Schlaftyp</h2>
  <ol class="panel__text sleeper__list">
    <li>1 Der Bauchschläfer<span>Mit dem Gesicht nach unten</span></li>
    <li>2 Der Fötus-Schläfer<span>Auf der Seite eingerollt</span></li>
    <li>3 Der Rückenschläfer<span>Auf dem Rücken,</span><span>Arme seitlich anliegend</span></li>
    <li>4 Der Seitenschläfer<span>Auf der Seite eingerollt</span></li>
  </ol>
</section>

</body>
</html>
```